Flyer-Design für Einzelhandel/Online-Shop für Werbetechnikzubehör
Zielgruppe
Wir sind ein Einzelhandel / Onlineshop für Werbetechnikzubehör. Plotterfolie, Plotter, DIY-Artikel. Wir kommen mitten aus dem Ruhrgebiet und unser Name verbindet das Plotten und unsere Herkunft. „Falzwerkstück“
Unsere Zielgruppe sind Kreative aus dem Bastel- / Nähbereich.
Aufgabenstellung
Wir legen wert auf die Verbindung zum Ruhrgebiet (Zechen und co.) Anbei stellen wir auch eine Datei zur Verfügung, die bereits auf unserem Auto und Gutscheinen implementiert ist. Gerne darf diese genutzt werden.
Wir legen Wert auf Gradlinigkeit und Übersichtlichkeit.
Unser Flyer soll ein A6 Format sein (Datenformat: 154 x 111 mm
3 mm Beschnitt) diesen wir mit einem Rabattcode versehen wollen.
Des Weiteren benötigen wir auch die Abbidung von Bildstrom / Netzkreis / Homepage.
Daher benötigen wir das Design natürlich auch in einem Bearbeitungsmodus für ai.
Gerade die Felder Rabattcode und Gutscheinbedingungen sollten beachtet werden.
10% auf alle Vinyl, Flex & Flockfolie (Bogenware)
Der Flyer wird als Versandbeileger für befreundete Unternehmen benötigt.
Wir möchten mit diesem Flyer Neukunden gewinnen.
Der Flyer kann beidseitig gestaltet werden. Hoch oder Quer ist auch frei wählbar.
Unsere Farben sind als Datei hochgeladen.

```html
<!DOCTYPE html>
<html lang="de">
<head>
<meta charset="utf-8">
<title>Falzwerkstück – Neukundenrabatt Flyer</title>
<link rel="stylesheet" href="https://fonts.googleapis.com/css2?family=Source+Sans+3:wght@300;400;600;700&display=swap">
<style>
  :root {
    --teal: #4a97a8;
    --ink: #585858;
    --band: #ededed;
    --paper: #ffffff;
    --stage: #ffffff;
    --text: #5e5e5e;
  }
  * { box-sizing: border-box; margin: 0; padding: 0; }
  html, body { width: 1140px; height: 1200px; overflow: hidden; background: var(--stage); }
  body { font-family: "Source Sans 3", sans-serif; position: relative; }

  .flyer {
    position: absolute;
    top: 411px;
    width: 530px;
    height: 377px;
    background: var(--paper);
    box-shadow: 0 0 4px rgba(0,0,0,0.35);
    overflow: hidden;
  }
  .flyer--front { left: 30px; }
  .flyer--back { left: 580px; }

  /* Front */
  .skyline {
    position: absolute;
    background: linear-gradient(180deg, rgba(88,88,88,0.15) 0%, rgba(88,88,88,0.55) 60%, rgba(88,88,88,0.8) 100%);
  }
  .flyer--front .skyline { left: 14px; right: 14px; top: 26px; height: 88px; }
  .front-baseline { position: absolute; left: 0; right: 0; top: 113px; height: 3px; background: var(--ink); }
  .front-band {
    position: absolute; left: 0; right: 0; top: 121px; height: 67px;
    background: var(--band);
    display: flex; align-items: center; justify-content: center;
  }
  .headline {
    color: var(--teal);
    font-weight: 700;
    letter-spacing: 2px;
  }
  .front-band .headline { font-size: 27px; }
  .brand-name {
    position: absolute; left: 0; right: 0; top: 290px;
    text-align: center;
    font-size: 32px; font-weight: 400; letter-spacing: 0.5px;
    color: var(--ink);
  }

  /* Back */
  .back-brand {
    position: absolute; left: 32px; top: 70px;
    font-size: 17px; font-weight: 600; color: var(--teal);
  }
  .flyer--back .skyline { left: 169px; top: 26px; width: 330px; height: 58px; }
  .back-rule { position: absolute; left: 150px; right: 31px; top: 84px; height: 2px; background: var(--teal); }
  .flyer--back .headline {
    position: absolute; right: 31px; top: 112px; font-size: 22px; letter-spacing: 1px;
  }
  .field { position: absolute; top: 164px; }
  .field__label { font-size: 12.5px; font-weight: 600; color: var(--teal); }
  .field__line { margin-top: 19px; height: 1px; background: var(--teal); }
  .field--date { left: 34px; width: 182px; }
  .field--code { left: 279px; width: 220px; }

  .terms { position: absolute; left: 34px; right: 31px; top: 232px; font-size: 9px; line-height: 1.2; color: var(--text); font-weight: 300; }
  .terms p + p { margin-top: 10px; }
  .terms strong { color: var(--teal); font-weight: 600; }

  .contact {
    position: absolute; right: 31px; top: 340px;
    display: flex; align-items: center; gap: 7px;
    font-size: 11.5px; color: var(--teal);
  }
  .contact .sep { opacity: 0.8; }
  .contact .web { font-weight: 600; }
  .social { display: flex; gap: 6px; margin-left: 10px; }
  .social__item { display: flex; align-items: center; gap: 3px; font-size: 10px; font-weight: 600; color: var(--ink); }
  .social__item i { width: 9px; height: 9px; background: var(--ink); display: inline-block; }
</style>
</head>
<body>

  <section class="flyer flyer--front" aria-label="Flyer Vorderseite">
    <div class="skyline" role="img" aria-label="Illustrierte Ruhrgebiets-Skyline mit Fördertürmen, Halde, Windrad und Fernsehturm"></div>
    <div class="front-baseline"></div>
    <div class="front-band"><h1 class="headline">NEUKUNDENRABATT</h1></div>
    <div class="brand-name">FALZWERKSTÜCK</div>
  </section>

  <section class="flyer flyer--back" aria-label="Flyer Rückseite">
    <div class="back-brand">Falzwerkstück</div>
    <div class="skyline" role="img" aria-label="Illustrierte Ruhrgebiets-Skyline mit Fördertürmen, Halde, Windrad und Fernsehturm"></div>
    <div class="back-rule"></div>
    <h2 class="headline">NEUKUNDENRABATT</h2>

    <div class="field field--date">
      <div class="field__label">DATUM</div>
      <div class="field__line"></div>
    </div>
    <div class="field field--code">
      <div class="field__label">RABATT-CODE</div>
      <div class="field__line"></div>
    </div>

    <div class="terms">
      <p><strong>BEDINGUNGEN:</strong> Lorem ipsum dolor sit amet, consectetuer adipiscing elit, sed diam nonummy nibh euismod incidunt ut laoreet dolore magna aliquam erat volutpat.</p>
      <p>Ut wisi enim ad minim veniam, quis nostrud exercitation ullamcorper suscipit lobortis nisl ut aliquip ex ea commodo consequat. Duis autem vel eum iriure dolor in.</p>
    </div>

    <div class="contact">
      <span>Zechenweg 37</span><span class="sep">|</span>
      <span>45127 Essen</span><span class="sep">|</span>
      <span class="web">www.falzwerkstueck.de</span>
      <span class="social">
        <span class="social__item"><i></i>Netzkreis</span>
        <span class="social__item"><i></i>Bildstrom</span>
      </span>
    </div>
  </section>

</body>
</html>
```